Brightvale Wound Care
Business cards and letterhead
Professional
Gregory Tamsett
Chief Executive Officer
3470 P Street NW
Suite 615
Washington, DC 20011
gtamsett@brightvale-wc.example
www.brightvale-wc.example
I need one that says "CEO" for the name above and one that says "Territory Manager". I also need (with the same design for the name Darren Pulcombe as "President" and one for him as well that says Senior Territory Manager"
I need to list these products on the back:
1. Verashu Negitive Pressure Wound Therapy
2. Brunix Negitive Pressure Wound Therapy
3. Orvil alternating pressure mattresses
Here is our logo please use this logo while doing our design for this project for both the business cards and letterhead. Thanks
Please add this one or the non-green one (also uploaded) some where on the card. Make it very small please.
Or add this one to the card somewhere. Whatever one looks better.

```html
<!DOCTYPE html>
<html lang="en">
<head>
<meta charset="utf-8">
<title>Brightvale Wound Care — Stationery</title>
<link href="https://fonts.googleapis.com/css2?family=Roboto:wght@400;500;700&display=swap" rel="stylesheet">
<style>
  :root {
    --navy: #2b2c8f;
    --red: #d9252b;
    --grey: #8a8a8a;
    --line: #d6d6d6;
    --paper: #ffffff;
    --page: #ffffff;
  }
  * { box-sizing: border-box; margin: 0; padding: 0; }
  html, body { width: 1200px; height: 806px; overflow: hidden; background: var(--page); }
  body { position: relative; font-family: "Roboto", Arial, sans-serif; color: var(--grey); }

  .brand { display: flex; align-items: center; justify-content: center; gap: 6px; color: var(--navy); font-weight: 700; white-space: nowrap; }
  .brand-dot { border-radius: 50%; background: var(--navy); flex: none; }

  .card { position: absolute; width: 216px; height: 156px; background: var(--paper); border: 1px solid var(--line); text-align: center; overflow: hidden; }
  .card .name { margin-top: 12px; font-size: 10px; font-weight: 700; color: var(--navy); }
  .card .name.accent { color: var(--red); }
  .card .title { margin-top: 2px; font-size: 6.5px; color: var(--grey); }
  .card .brand { margin-top: 18px; font-size: 12px; }
  .card .brand-dot { width: 12px; height: 12px; }
  .card .contact { position: absolute; left: 0; right: 0; bottom: 14px; font-size: 5.5px; line-height: 1.5; color: var(--grey); }

  .card-back .brand { margin-top: 40px; }
  .card-back .products { margin-top: 14px; font-size: 6px; line-height: 1.5; color: var(--red); }
  .card-back .band { position: absolute; left: 0; right: 0; bottom: 0; height: 44px; background: var(--navy); border-top: 3px solid var(--red); color: #fff; font-size: 6px; line-height: 1.5; padding-top: 8px; }

  .envelope { position: absolute; left: 41px; top: 440px; width: 655px; height: 280px; }
  .envelope svg { position: absolute; left: 0; top: 0; }
  .envelope .brand { position: absolute; left: 0; right: 0; top: 124px; font-size: 22px; }
  .envelope .brand-dot { width: 20px; height: 20px; }
  .envelope .return { position: absolute; left: 172px; bottom: 18px; font-size: 7px; color: var(--grey); }

  .letterhead { position: absolute; left: 725px; top: 43px; width: 423px; height: 720px; background: var(--paper); border: 1px solid var(--line); }
  .letterhead .brand { margin-top: 46px; font-size: 20px; }
  .letterhead .brand-dot { width: 18px; height: 18px; }
  .letterhead .fold { position: absolute; left: -1px; width: 8px; border-top: 1px solid var(--grey); }
  .letterhead .footer { position: absolute; left: 0; right: 0; bottom: 12px; text-align: center; font-size: 7px; line-height: 1.55; color: var(--grey); }
  .letterhead .footer .label { color: var(--red); }
  .letterhead .footer .web { color: var(--navy); }
</style>
</head>
<body>

  <!-- Business cards, fronts -->
  <section class="card" style="left:43px; top:91px;">
    <p class="name">Gregory Tamsett</p>
    <p class="title">Chief Executive Officer</p>
    <div class="brand"><span class="brand-dot"></span>Brightvale Wound Care</div>
    <p class="contact">3470 P Street NW Suite 615 Washington, DC 20011<br>P: 202.555.0143 F: 202.555.0162 E: gtamsett@brightvale-wc.example<br>www.brightvale-wc.example</p>
  </section>

  <section class="card" style="left:274px; top:91px;">
    <p class="name">Darren Pulcombe</p>
    <p class="title">President</p>
    <div class="brand"><span class="brand-dot"></span>Brightvale Wound Care</div>
    <p class="contact">3470 P Street NW Suite 615 Washington, DC 20011<br>P: 202.555.0143 F: 202.555.0162<br>www.brightvale-wc.example</p>
  </section>

  <section class="card card-back" style="left:506px; top:91px;">
    <div class="brand"><span class="brand-dot"></span>Brightvale Wound Care</div>
    <p class="products">Verashu Negative Pressure Wound Therapy<br>Brunix Negative Pressure Wound Therapy<br>Orvil alternating pressure mattresses</p>
  </section>

  <section class="card" style="left:43px; top:264px;">
    <p class="name accent">Gregory Tamsett</p>
    <p class="title">Territory Manager</p>
    <div class="brand"><span class="brand-dot"></span>Brightvale Wound Care</div>
    <p class="contact">3470 P Street NW Suite 615 Washington, DC 20011<br>P: 202.555.0143 F: 202.555.0162 E: gtamsett@brightvale-wc.example<br>www.brightvale-wc.example</p>
  </section>

  <section class="card" style="left:274px; top:264px;">
    <p class="name">Darren Pulcombe</p>
    <p class="title">Senior Territory Manager</p>
    <div class="brand"><span class="brand-dot"></span>Brightvale Wound Care</div>
    <p class="contact">3470 P Street NW Suite 615 Washington, DC 20011<br>P: 202.555.0143 F: 202.555.0162<br>www.brightvale-wc.example</p>
  </section>

  <section class="card card-back" style="left:506px; top:264px;">
    <div class="brand" style="margin-top:34px;"><span class="brand-dot"></span>Brightvale Wound Care</div>
    <div class="band">Verashu Negative Pressure Wound Therapy<br>Brunix Negative Pressure Wound Therapy<br>Orvil alternating pressure mattresses</div>
  </section>

  <!-- Envelope -->
  <section class="envelope">
    <svg width="655" height="280" viewBox="0 0 655 280">
      <rect x="0.5" y="88" width="654" height="191.5" fill="#ffffff" stroke="#d6d6d6"/>
      <path d="M0 88 C 90 40, 220 10, 330 14 C 450 10, 570 40, 655 88 Z" fill="var(--navy)"/>
    </svg>
    <div class="brand"><span class="brand-dot"></span>Brightvale Wound Care</div>
    <p class="return">3470 P Street NW Suite 615 Washington, DC 20011</p>
  </section>

  <!-- Letterhead -->
  <section class="letterhead">
    <span class="fold" style="top:120px;"></span>
    <span class="fold" style="top:448px;"></span>
    <div class="brand"><span class="brand-dot"></span>Brightvale Wound Care</div>
    <p class="footer">3470 P Street NW Suite 615 Washington, DC 20011<br><span class="label">P:</span> 202.555.0143 <span class="label">F:</span> 202.555.0162 <span class="label">E:</span> gtamsett@brightvale-wc.example<br><span class="web">www.brightvale-wc.example</span></p>
  </section>

</body>
</html>
```